Business Card

We need some ideas for corporate business cards. I'm interested in a double sided card, with one side featuring our corporate logo, the other side with employee information.

Corporate colors, logo etc. available at www.brivalo.com

Industry/Entity Type

Business

Requirements
Must have
• The "Brivalo" logo with stylized "O"

Nice to have
• Preferred font is calibri

```html
<!DOCTYPE html>
<html lang="en">
<head>
<meta charset="utf-8">
<title>Brivalo Business Card</title>
<link href="https://fonts.googleapis.com/css2?family=Carlito:wght@400;700&display=swap" rel="stylesheet">
<style>
  :root {
    --backdrop: #1f2a38;
    --card: #efefef;
    --card-edge: #f7f7f7;
    --teal: #0f6e72;
    --teal-band: #046464;
    --teal-bright: #0a7c78;
    --grey-band: #707070;
    --text-dark: #333333;
    --social-blue: #3b5998;
    --social-sky: #1b8ed1;
    --white: #ffffff;
  }
  html, body {
    margin: 0;
    padding: 0;
    width: 1200px;
    height: 970px;
    overflow: hidden;
    background: var(--backdrop);
    font-family: "Carlito", Calibri, sans-serif;
  }
  .canvas {
    position: relative;
    width: 1200px;
    height: 970px;
  }
  .card {
    position: absolute;
    background: linear-gradient(135deg, var(--card-edge), var(--card) 60%, #e6e6e6);
    box-shadow: 0 6px 18px rgba(0,0,0,0.45);
    overflow: hidden;
  }
  .card--front { left: 103px; top: 55px; width: 677px; height: 406px; }
  .card--back  { left: 409px; top: 487px; width: 678px; height: 406px; }

  .stripe { position: absolute; left: 0; width: 269px; height: 24px; }
  .stripe--teal { background: linear-gradient(90deg, var(--teal-bright) 57%, var(--teal-band) 57%); }
  .stripe--grey { background: linear-gradient(90deg, var(--grey-band) 57%, #5e5e5e 57%); }

  .logo-panel {
    position: absolute;
    background: var(--teal);
    display: flex;
    align-items: center;
    justify-content: center;
  }
  .logo-name {
    color: var(--white);
    font-weight: 700;
    font-size: 50px;
    letter-spacing: 6px;
    text-transform: uppercase;
  }
  .card--front .logo-panel { left: 306px; top: 133px; width: 371px; height: 119px; }
  .card--back .logo-panel  { left: 163px; top: 0; width: 372px; height: 119px; }

  .social {
    position: absolute;
    display: flex;
    align-items: center;
    gap: 9px;
    font-weight: 700;
  }
  .social__mark { width: 36px; height: 36px; border-radius: 5px; }
  .social--page { left: 70px; top: 355px; color: var(--social-blue); font-size: 20px; letter-spacing: 1.5px; }
  .social--page .social__mark { background: var(--social-blue); }
  .social--feed { left: 442px; top: 352px; color: var(--social-sky); font-size: 18px; }
  .social--feed .social__mark { background: var(--social-sky); border-radius: 50%; }

  .band { position: absolute; left: 0; width: 100%; background: var(--teal-band); }
  .band--upper { top: 162px; height: 34px; }
  .band--lower { top: 205px; height: 35px; }
  .band-rule {
    position: absolute; left: 0; top: 196px; width: 100%; height: 9px;
    background: linear-gradient(90deg, #8a8a8a, #e0e0e0 40%, #9a9a9a 70%, #d8d8d8);
  }

  .contact {
    position: absolute;
    left: 206px;
    top: 258px;
    margin: 0;
    padding: 0;
    list-style: none;
    color: var(--text-dark);
    font-weight: 700;
    font-size: 16px;
    line-height: 15px;
  }
  .contact__item { display: flex; align-items: flex-start; gap: 12px; }
  .contact__item + .contact__item { margin-top: 14px; }
  .contact__icon { width: 20px; height: 20px; flex: none; fill: var(--text-dark); margin-top: -2px; }
  .contact__item--address { margin-bottom: 0; }
</style>
</head>
<body>
<main class="canvas">

  <section class="card card--front" aria-label="Card front">
    <div class="stripe stripe--teal" style="top:144px"></div>
    <div class="stripe stripe--grey" style="top:180px"></div>
    <div class="stripe stripe--teal" style="top:216px"></div>

    <div class="logo-panel"><span class="logo-name">Brivalo</span></div>

    <div class="social social--page"><span class="social__mark"></span><span>BrivaloInc</span></div>
    <div class="social social--feed"><span class="social__mark"></span><span>brivaloglobal</span></div>
  </section>

  <section class="card card--back" aria-label="Card back">
    <div class="logo-panel"><span class="logo-name">Brivalo</span></div>

    <div class="band band--upper"></div>
    <div class="band-rule"></div>
    <div class="band band--lower"></div>

    <ul class="contact">
      <li class="contact__item contact__item--address">
        <svg class="contact__icon" viewBox="0 0 20 20" aria-hidden="true"><path d="M10 1 L19 10 L16 10 L16 19 L12 19 L12 13 L8 13 L8 19 L4 19 L4 10 L1 10 Z"/></svg>
        <span>14 Harlow Lane, Crestfield Business Park,<br>Corran 12, Ireland</span>
      </li>
      <li class="contact__item">
        <svg class="contact__icon" viewBox="0 0 20 20" aria-hidden="true"><path d="M5 0 H15 A1 1 0 0 1 16 1 V19 A1 1 0 0 1 15 20 H5 A1 1 0 0 1 4 19 V1 A1 1 0 0 1 5 0 Z M6 2 V16 H14 V2 Z M9 17 H11 V19 H9 Z"/></svg>
        <span>+353 1 555 0142</span>
      </li>
      <li class="contact__item">
        <svg class="contact__icon" viewBox="0 0 20 20" aria-hidden="true"><path d="M0 2 H20 V15 H12 V17 H15 V19 H5 V17 H8 V15 H0 Z M2 4 V13 H18 V4 Z"/></svg>
        <span>www.brivalo.com</span>
      </li>
      <li class="contact__item">
        <svg class="contact__icon" viewBox="0 0 20 20" aria-hidden="true"><text x="10" y="16" text-anchor="middle" font-family="Carlito, sans-serif" font-weight="700" font-size="18">@</text></svg>
        <span>info@brivalo.com</span>
      </li>
    </ul>
  </section>

</main>
</body>
</html>
```